Velnor Modellwerk.Brenn GmbH needed a letterhead template

For English scroll down. We need a letterhead template and since we already have our logo design successfully with you, we now want to also design the letterhead with you. Down in the uploaded file you see what is important and what should definitely be seen on our template. The template should be like the homepage (www.modellwerk.brenn) held in red, blue and white. We need a letter-head submission. In the bottom in the chapter "databases uploading" you can find the most important things, did must be on the submission. The submission shoulderstand be in the colors blue, red and white like our homepage (www.modellwerk.brenn).

```html
<!DOCTYPE html>
<html lang="de">
<head>
<meta charset="utf-8">
<title>Velnor Modellwerk.Brenn GmbH – Briefpapier</title>
<link href="https://fonts.googleapis.com/css2?family=Roboto:wght@400;500&display=swap" rel="stylesheet">
<style>
  :root {
    --brand-red: #c51f27;
    --brand-blue: #1f6db5;
    --paper: #fafafa;
    --backdrop: #e9e9e9;
    --ink: #3f3f3f;
  }
  html, body {
    margin: 0;
    width: 1200px;
    height: 1172px;
    overflow: hidden;
    background: var(--backdrop);
    font-family: "Roboto", Arial, sans-serif;
  }
  .letterhead {
    position: absolute;
    left: 216px;
    top: 42px;
    width: 768px;
    height: 1087px;
    background: var(--paper);
    overflow: hidden;
  }
  .brand {
    position: absolute;
    left: 44px;
    top: 50px;
    display: flex;
    align-items: center;
    gap: 10px;
  }
  .brand-dot {
    width: 22px;
    height: 22px;
    border-radius: 50%;
    background: var(--brand-red);
  }
  .brand-name {
    font-size: 29px;
    font-weight: 500;
    color: var(--brand-red);
    letter-spacing: 0.2px;
  }
  .sender-address {
    position: absolute;
    right: 57px;
    top: 56px;
    padding: 2px 6px 5px 0;
    border-right: 2px solid var(--brand-red);
    text-align: right;
    font-size: 11.5px;
    line-height: 14px;
    font-style: normal;
    color: var(--ink);
  }
  .footer-column {
    position: absolute;
    top: 985px;
    padding: 2px 0 6px 11px;
    border-left: 2px solid var(--brand-blue);
    font-size: 10px;
    line-height: 12.7px;
    color: var(--ink);
  }
  .footer-column.company { left: 43px; }
  .footer-column.bank { left: 313px; }
  .footer-column.contact { left: 548px; border-left-color: var(--brand-red); padding-bottom: 4px; }
  .footer-band {
    position: absolute;
    left: 0;
    bottom: 0;
    width: 768px;
    height: 36px;
  }
  .web-address {
    position: absolute;
    left: 560px;
    bottom: 9px;
    font-size: 10.5px;
    color: #ffffff;
  }
</style>
</head>
<body>
  <main class="letterhead">
    <header class="brand">
      <span class="brand-dot"></span>
      <span class="brand-name">Modellwerk.Brenn</span>
    </header>

    <address class="sender-address">
      Velnor Modellwerk.Brenn GmbH<br>
      Feldgasse 12<br>
      6175 Kemnat, Tirol<br>
      Österreich
    </address>

    <footer>
      <div class="footer-column company">
        Geschäftsführer Dr. Lenz Marius<br>
        Feldgasse 12<br>
        6175 Kemnat, Tirol<br>
        Österreich
      </div>
      <div class="footer-column bank">
        Alpbank 5678<br>
        IBAN: AT61 5555 6666 7777<br>
        BIC: 5678<br>
        UID-Nr.: ATU654321
      </div>
      <div class="footer-column contact">
        Telefon: 0800 44 55 666<br>
        Mail: contact@modellwerk.brenn
      </div>

      <svg class="footer-band" viewBox="0 1051 768 36" aria-hidden="true">
        <rect x="0" y="1076" width="500" height="11" fill="var(--brand-blue)"/>
        <path d="M478 1087 L510 1062 Q520 1052 538 1052 L768 1052 L768 1087 Z" fill="var(--brand-red)"/>
      </svg>
      <span class="web-address">www.modellwerk.brenn</span>
    </footer>
  </main>
</body>
</html>
```